Business Card Design Project

This is the first time we use our new logo. We need a business card that we can use both on our institutional corporate relationships and also that works for our staff that deals with consumers directly.

VELUNDA is a new company dedicated to empower consumers and to provide them with the best choices for specialized health care using the latest telemedicine technology (medicine at a distance via videoconference).

We want to print this cards in high quality materials and process. We will like designs that allow us to use UV spot varnish and other techniques that will differentiate us.

We are including Two different versions of Color logos. In addition we are including white over black background logos. Those can be used replacing the black for a color.

Please note this is the first time we will be creating any corporate materials with our new logo and colors.

Target Market(s)

34+ consumers of medium high and high socioeconomic levels.

Industry/Entity Type

Health

Requirements
Must have
• Our logo on its original colors
Should not have
• Any other graphical element or design that is not our logo

```html
<!DOCTYPE html>
<html lang="en">
<head>
<meta charset="utf-8">
<title>VELUNDA Business Card</title>
<link rel="stylesheet" href="https://fonts.googleapis.com/css2?family=Jost:wght@400;500;600&family=PT+Sans&display=swap">
<style>
  :root {
    --stage: #ece9e4;
    --brand-blue: #1d5a86;
    --brand-teal: #2aa398;
    --ink: #1a1a1a;
    --white: #ffffff;
    --metal-light: #e4e4e4;
    --metal-mid: #c4c4c4;
    --metal-dark: #3c3c3c;
  }
  * { margin: 0; padding: 0; box-sizing: border-box; }
  html, body { width: 1200px; height: 788px; overflow: hidden; }
  body {
    position: relative;
    background: var(--stage);
    font-family: "Jost", "Helvetica Neue", Arial, sans-serif;
    color: var(--ink);
  }
  .view-label {
    position: absolute;
    width: 524px;
    text-align: center;
    font-family: "PT Sans", Arial, sans-serif;
    font-size: 20px;
    color: #222;
  }
  .card {
    position: absolute;
    width: 524px;
    height: 300px;
    border-radius: 20px;
    overflow: hidden;
  }
  .card--front { left: 54px; top: 74px; background: linear-gradient(100deg, #cfcfcf, var(--metal-light) 45%, #bdbdbd); }
  .card--back-white { left: 622px; top: 74px; background: var(--white); }
  .card--back-metal { left: 54px; top: 445px; background: linear-gradient(180deg, #f2f2f2 0%, var(--metal-mid) 40%, #8a8a8a 70%, var(--metal-dark) 100%); }
  .card--back-blue { left: 622px; top: 445px; background: var(--brand-blue); }

  .swoosh { position: absolute; inset: 0; }

  .brand-dot {
    position: absolute;
    border-radius: 50%;
    background: var(--brand-teal);
  }
  .wordmark {
    position: absolute;
    font-weight: 600;
    color: var(--brand-blue);
    letter-spacing: 2px;
    line-height: 1;
    white-space: nowrap;
  }
  .wordmark--light { color: var(--white); }

  .holder-name { position: absolute; left: 36px; top: 152px; font-size: 17px; font-weight: 600; }
  .holder-name span { font-size: 14px; font-weight: 400; }
  .contact-line { position: absolute; left: 36px; font-size: 13.5px; white-space: nowrap; }
  .contact-line b { font-style: italic; font-weight: 600; }

  .web {
    position: absolute;
    left: 0; width: 100%;
    text-align: center;
    font-size: 16px;
    letter-spacing: 3px;
  }
  .web--dark { color: #333; }
  .web--light { color: var(--white); }
</style>
</head>
<body>
  <div class="view-label" style="left:54px;top:34px;">Front</div>
  <div class="view-label" style="left:622px;top:34px;">Back - 1</div>
  <div class="view-label" style="left:54px;top:405px;">Back - 2</div>
  <div class="view-label" style="left:622px;top:405px;">Back - 3</div>

  <section class="card card--front">
    <svg class="swoosh" width="524" height="300" viewBox="0 0 524 300" aria-hidden="true">
      <path d="M395,0 C470,30 520,140 478,300 H524 V0 Z" fill="#1d5a86"/>
      <path d="M412,0 C478,40 510,150 472,300" fill="none" stroke="#d6d6d6" stroke-width="7"/>
    </svg>
    <div class="brand-dot" style="left:42px;top:60px;width:60px;height:60px;"></div>
    <div class="wordmark" style="left:114px;top:78px;font-size:40px;">VELUNDA</div>
    <div class="holder-name">Your Name, <span>Designation</span></div>
    <div class="contact-line" style="top:197px;"><b>p</b> : +12 345 67890 &nbsp;&nbsp;| <b>f</b> : +12 345 67890</div>
    <div class="contact-line" style="top:225px;"><b>e</b> : info@velundahealth.com &nbsp;| <b>w</b> : www.velundahealth.com</div>
    <div class="contact-line" style="top:253px;">#0000, Street Name, Area Name, Country Code</div>
  </section>

  <section class="card card--back-white">
    <div class="brand-dot" style="left:100px;top:100px;width:72px;height:72px;"></div>
    <div class="wordmark" style="left:190px;top:112px;font-size:50px;">VELUNDA</div>
    <div class="web web--dark" style="top:258px;">www.velundahealth.com</div>
  </section>

  <section class="card card--back-metal">
    <div class="brand-dot" style="left:100px;top:110px;width:72px;height:72px;"></div>
    <div class="wordmark" style="left:190px;top:122px;font-size:46px;">VELUNDA</div>
    <div class="web web--light" style="top:262px;">www.velundahealth.com</div>
  </section>

  <section class="card card--back-blue">
    <div class="brand-dot" style="left:222px;top:40px;width:80px;height:80px;"></div>
    <div class="wordmark wordmark--light" style="left:0;width:100%;text-align:center;top:174px;font-size:48px;">VELUNDA</div>
    <div class="web web--light" style="top:262px;">www.velundahealth.com</div>
  </section>
</body>
</html>
```